ターゲットは、墓地を探している方です。生前墓、小規模墓地、ペットと共に墓地に入れる敷地も用意されています。
http://www.asahidaireien.jp/
1ページ
緑 青
• イラストレーター形式 (.ai)
サイトレイアウトのPDFデータです。

弊社お客様にデザインを選んでいただきました。
お客様のイメージと一致したようでとても喜んでいただきました。

すばらしいデザインをありがとうございました。
24デザインの中からお客様に選んでいただきました。
お客様はとても喜んでおります。
今後ともよろしくお願いします。

```html
<!DOCTYPE html>
<html lang="ja">
<head>
<meta charset="utf-8">
<title>朝日台霊苑</title>
<link href="https://fonts.googleapis.com/css2?family=Noto+Sans+JP:wght@400;500;700&family=Noto+Serif+JP:wght@600&display=swap" rel="stylesheet">
<style>
:root{
  --green:#2f7d3a;
  --green-dark:#1f6a2c;
  --green-light:#e6f1e3;
  --line:#cfd8cc;
  --text:#444;
  --muted:#888;
  --bg:#ffffff;
}
*{box-sizing:border-box;margin:0;padding:0}
html,body{width:831px;height:1200px;overflow:hidden;background:var(--bg);font-family:"Noto Sans JP",sans-serif;color:var(--text);font-size:11px}
.page{width:675px;margin:0 auto;position:relative;height:1200px}
.site-header{height:92px;display:flex;justify-content:space-between;align-items:center}
.brand{display:flex;align-items:center;gap:8px;font-family:"Noto Serif JP",serif;font-weight:600;font-size:26px;color:var(--green)}
.brand-mark{width:22px;height:22px;background:var(--green)}
.contact{text-align:right}
.contact small{display:block;font-size:9px;color:var(--muted)}
.contact .tel{display:flex;align-items:center;gap:6px;font-size:24px;font-weight:700;color:var(--green);letter-spacing:1px}
.global-nav{display:flex;border-top:1px solid var(--line);border-bottom:1px solid var(--line);height:30px}
.global-nav a{flex:1;text-align:center;line-height:30px;font-size:10px;color:var(--text);text-decoration:none;border-right:1px solid var(--line)}
.global-nav a:last-child{border-right:none}
.hero{display:flex;height:190px;margin-top:12px}
.hero-photo{flex:1.55;background:linear-gradient(180deg,#d9e6ef 0%,#c4d8b5 45%,#7a9a63 80%,#9aa49a 100%)}
.hero-flowers{flex:1;background:linear-gradient(100deg,#f4eed3 0%,#ecdaf0 40%,#e0a7cf 70%,#c97fb6 100%)}
.body{display:flex;gap:22px;margin-top:26px}
.sidebar{width:143px}
.side-box{border:1px solid var(--line);margin-bottom:14px}
.side-box h3{background:var(--green-light);color:var(--green-dark);font-size:11px;padding:5px 8px;border-bottom:1px solid var(--line)}
.voice{display:flex;align-items:center;gap:8px;padding:7px 8px;border-bottom:1px dotted var(--line);font-size:9px;color:var(--green)}
.voice:last-child{border-bottom:none}
.voice .avatar{width:26px;height:26px;border-radius:50%;background:#e7d9c8;flex:none}
.access-photo{height:70px;margin:8px;background:linear-gradient(180deg,#c9d9e6,#a9bd9c)}
.access-text{font-size:8.5px;line-height:1.6;padding:0 8px 8px;color:var(--muted)}
.main{flex:1}
.section-title{font-size:15px;font-weight:700;color:var(--green-dark);border-bottom:2px solid var(--green);padding:0 0 5px 10px;position:relative;margin-bottom:12px}
.section-title::before{content:"";position:absolute;left:0;top:4px;width:4px;height:15px;background:var(--green)}
.about{display:flex;gap:12px;margin-bottom:22px}
.about p{flex:1;font-size:9px;line-height:1.9;color:var(--muted)}
.about-photo{width:150px;height:100px;background:linear-gradient(180deg,#d3e2ee,#9fbd8a 70%,#8a9a86)}
.diff-box{border:1px solid var(--line);padding:12px;margin-bottom:22px}
.diff-box h4{font-size:12px;color:var(--green-dark);margin:0 0 10px 130px}
.diff-row{display:flex;gap:14px;margin-bottom:10px}
.diff-row:last-child{margin-bottom:0}
.diff-illust{width:116px;height:70px;flex:none;background:linear-gradient(180deg,#eef2ea,#c9d6c0)}
.diff-row p{font-size:9px;line-height:1.8;color:var(--muted)}
.topics{list-style:none}
.topics li{display:flex;gap:18px;border-bottom:1px dotted var(--line);padding:8px 6px;font-size:9px}
.topics time{color:var(--muted);width:80px}
.topics span{color:var(--text)}
.site-footer{position:absolute;left:-78px;right:-78px;top:1112px;height:88px;background:var(--green);color:#fff;text-align:center}
.footer-nav{padding-top:18px;font-size:9px;display:flex;justify-content:center;gap:18px}
.site-footer small{display:block;margin-top:20px;font-size:8px;opacity:.85}
.pagetop{position:absolute;right:0;top:1090px;font-size:8px;color:var(--green)}
</style>
</head>
<body>
<div class="page">
  <header class="site-header">
    <div class="brand"><span class="brand-mark"></span>朝日台霊苑</div>
    <div class="contact">
      <small>お気軽にご相談ください</small>
      <div class="tel">
        <svg width="20" height="20" viewBox="0 0 24 24"><rect x="0" y="0" width="24" height="24" fill="#2f7d3a"/><path d="M7 5l3 3-2 2c1 2 3 4 5 5l2-2 3 3-2 3C10 18 5 13 4 7z" fill="#fff"/></svg>
        0120-48-2210
      </div>
    </div>
  </header>
  <nav class="global-nav">
    <a href="#">ホーム</a><a href="#">霊園概要</a><a href="#">施設・アクセス</a><a href="#">墓所案内</a><a href="#">永代供養</a><a href="#">資料請求</a><a href="#">よくある質問</a><a href="#">お問合せ</a>
  </nav>
  <div class="hero">
    <div class="hero-photo" role="img" aria-label="緑に囲まれた霊園の墓所の写真"></div>
    <div class="hero-flowers" role="img" aria-label="白や紫の花の写真"></div>
  </div>
  <div class="body">
    <aside class="sidebar">
      <div class="side-box">
        <h3>お客様の声</h3>
        <div class="voice"><span class="avatar" role="img" aria-label="お客様の写真"></span>千葉県在住の方へ</div>
        <div class="voice"><span class="avatar" role="img" aria-label="お客様の写真"></span>東京都在住の方へ</div>
        <div class="voice"><span class="avatar" role="img" aria-label="お客様の写真"></span>千葉県在住の方へ</div>
      </div>
      <div class="side-box">
        <h3>交通アクセス</h3>
        <div class="access-photo" role="img" aria-label="霊園入口の写真"></div>
        <p class="access-text">駅から車で約20分。無料送迎バスも運行しております。駐車場完備、お車でも安心してお越しいただけます。</p>
      </div>
    </aside>
    <main class="main">
      <h2 class="section-title">朝日台霊苑について</h2>
      <div class="about">
        <p>緑豊かな丘の上に広がる霊園です。生前墓や小規模墓地、ペットと一緒に眠れる区画もご用意しております。四季折々の花に囲まれた穏やかな環境で、大切な方を末永く供養いただけます。見学はいつでも承っております。</p>
        <div class="about-photo" role="img" aria-label="霊園の全景写真"></div>
      </div>
      <div class="diff-box">
        <h4>霊園と墓地の違い</h4>
        <div class="diff-row"><div class="diff-illust" role="img" aria-label="寺院墓地のイラスト"></div><p>寺院墓地はお寺の境内にあり、檀家になることが前提となる場合が多く、宗派の決まりに沿って供養を行います。</p></div>
        <div class="diff-row"><div class="diff-illust" role="img" aria-label="公営霊園のイラスト"></div><p>公営霊園は自治体が運営し、使用料が比較的安い一方、募集時期や応募条件が限られることがあります。</p></div>
        <div class="diff-row"><div class="diff-illust" role="img" aria-label="民営霊園のイラスト"></div><p>民営霊園は宗派を問わず利用でき、区画の大きさや墓石のデザインを自由に選べるのが特徴です。</p></div>
      </div>
      <h2 class="section-title">トピックス</h2>
      <ul class="topics">
        <li><time>2013年7月1日</time><span>ホームページを公開しました</span></li>
        <li><time>2013年7月1日</time><span>ここにお知らせの見出しが入ります</span></li>
        <li><time>2013年7月1日</time><span>お盆期間の見学受付について</span></li>
        <li><time>2013年7月1日</time><span>ここにお知らせの見出しが入ります</span></li>
        <li><time>2013年7月1日</time><span>ここにお知らせの見出しが入ります</span></li>
      </ul>
    </main>
  </div>
  <span class="pagetop">▲ ページの先頭へ</span>
  <footer class="site-footer">
    <div class="footer-nav"><span>ホーム</span><span>霊園概要</span><span>施設・アクセス</span><span>墓所案内</span><span>永代供養</span><span>資料請求</span><span>お問合せ</span></div>
    <small>Copyright © 朝日台霊苑 All Rights Reserved.</small>
  </footer>
</div>
</body>
</html>
```